Wandrift: Travel business card redesign

We need a clean elegant look for our cards featuring blue and orange. Look should communicate a sense of strong design and seem uncluttered. The company is Wandrift which means drift to wander. As in every trip is an drift to wander. Feel free to reinvent the logo or just tweak it. Colors should be blue like Caribbean waters and a saturated orange. Keep it clean and simple.
Please match the information in the sample uploaded but the sample is horrible -- a non-starter -- use for information only. also please add managing director to my name as title

Target Market(s)
potential clients, hotels, trade publications
Industry/Entity Type
Travel Industry
Contact Information for Business Card
as above
Requirements
Must have
- Font should be century gothic. Colors below are close but a but prefer lighter in each case.

```html
<!DOCTYPE html>
<html lang="en">
<head>
<meta charset="utf-8">
<title>Wandrift Business Card</title>
<link href="https://fonts.googleapis.com/css2?family=Montserrat:wght@700&family=Questrial&display=swap" rel="stylesheet">
<style>
  :root {
    --backdrop: #6e4c36;
    --orange: #eb8b2e;
    --paper: #f3f3f3;
    --caribbean: #5fa6d6;
    --white: #ffffff;
    --card-shadow: rgba(0, 0, 0, 0.45);
  }
  * { margin: 0; padding: 0; box-sizing: border-box; }
  html, body { width: 1200px; height: 960px; overflow: hidden; }
  body {
    background: var(--backdrop);
    position: relative;
    font-family: "Questrial", "Century Gothic", sans-serif;
  }
  .card {
    position: absolute;
    width: 600px;
    height: 341px;
    border-radius: 22px;
    overflow: hidden;
    box-shadow: 2px 4px 6px var(--card-shadow);
  }
  .card--front { left: 314px; top: 114px; background: var(--paper); }
  .card--back { left: 312px; top: 473px; width: 598px; height: 340px; background: var(--orange); }

  .wordmark {
    position: absolute;
    font-family: "Montserrat", "Century Gothic", sans-serif;
    font-weight: 700;
    letter-spacing: -2px;
    line-height: 1;
    white-space: nowrap;
  }
  .tagline {
    position: absolute;
    font-family: "Questrial", "Century Gothic", sans-serif;
    line-height: 1;
    white-space: nowrap;
  }
  .card--front .wordmark { left: 154px; top: 50px; font-size: 56px; color: var(--orange); }
  .card--front .tagline { left: 252px; top: 102px; font-size: 24px; color: var(--caribbean); }

  .divider-band {
    position: absolute; left: 0; top: 190px; width: 100%; height: 5px;
    background: var(--caribbean);
    border-bottom: 1px solid var(--white);
  }
  .info-panel {
    position: absolute; left: 0; top: 195px; width: 100%; height: 146px;
    background: var(--orange); color: var(--white);
  }
  .holder-name {
    position: absolute; top: 20px; width: 100%; text-align: center;
    font-family: "Montserrat", "Century Gothic", sans-serif;
    font-weight: 700; font-size: 18px; letter-spacing: 0.5px;
  }
  .title-rule {
    position: absolute; left: 24px; right: 24px; top: 45px;
    display: flex; align-items: center; gap: 4px;
    font-size: 15px; letter-spacing: 0.5px;
  }
  .title-rule::before, .title-rule::after {
    content: ""; flex: 1; height: 1px; background: rgba(255,255,255,0.75);
  }
  .address {
    position: absolute; left: 24px; top: 65px;
    font-size: 15px; line-height: 18px; font-style: normal;
  }
  .contact-list {
    position: absolute; right: 22px; top: 65px;
    list-style: none; font-size: 15px; line-height: 19px; text-align: right;
  }
  .contact-list li { display: flex; justify-content: flex-end; align-items: center; gap: 6px; }
  .contact-list svg { width: 13px; height: 13px; fill: var(--white); }

  .card--back .wordmark { left: 136px; top: 122px; font-size: 62px; color: var(--white); }
  .card--back .tagline { left: 244px; top: 180px; font-size: 26px; color: var(--white); }
  .back-slogan {
    position: absolute; top: 280px; width: 100%; text-align: center;
    font-size: 17px; color: var(--white);
  }
</style>
</head>
<body>
  <section class="card card--front">
    <div class="wordmark">Wandrift</div>
    <div class="tagline">drift to wander</div>
    <div class="divider-band"></div>
    <div class="info-panel">
      <div class="holder-name">REID CALLOWAY</div>
      <div class="title-rule">MANAGING DIRECTOR</div>
      <address class="address">
        1416 Harbor Crest<br>Way N.<br>Bay Shore, 90611
      </address>
      <ul class="contact-list">
        <li>877.92.DRIFT (37438)
          <svg viewBox="0 0 12 12" aria-label="phone"><path d="M2.5 0.5l2 2-1 1.5c0.6 1.5 1.9 2.8 3.5 3.5l1.5-1 2 2-1.5 2C5 10 2 7 0.5 2z"/></svg>
        </li>
        <li>415.208.3350
          <svg viewBox="0 0 12 12" aria-label="mobile"><path d="M3 0h6v12H3z M4 1.5v8h4v-8z"/></svg>
        </li>
        <li>510.482.6613
          <svg viewBox="0 0 12 12" aria-label="fax"><path d="M3 1h6v3H3z M1 5h10v5H1z M3 8h6v3H3z"/></svg>
        </li>
      </ul>
    </div>
  </section>

  <section class="card card--back">
    <div class="wordmark">Wandrift</div>
    <div class="tagline">drift to wander</div>
    <p class="back-slogan">A leader in travel service</p>
  </section>
</body>
</html>
```